Custom unique Stationary design for Logistics company

We need a custom, unique , elegant and luxurious full stationary design using our new logo, following these guidelines:
1- Business card: double sided, both sides uses the navy blue as the background main color (same as the code of the navy blue used in our logo).
2- envelope and folder: also use the same navy blue as the main background color.
3- book cover( notepad cover) : same thing with the navy blue
4- letterhead: feel free to use the combination of the colors in our logo.
5- rest of the items are up to your creativity

Target Market(s)

corporates and other businesses

Industry/Entity Type

Logistics and heavy machines contractors

Requirements
Must have
• Letterhead, business card, envelope, notepad cover, paper, file
Nice to have
• navy blue to be main background color for business card, envelope, notepad cover

```html
<!DOCTYPE html>
<html lang="en">
<head>
<meta charset="utf-8">
<title>Quorvane Freight Company – Business Card</title>
<link href="https://fonts.googleapis.com/css2?family=Arimo:wght@400;700&family=Montserrat:wght@800;900&display=swap" rel="stylesheet">
<style>
  :root {
    --navy: #02527a;
    --navy-deep: #013f5e;
    --navy-light: #0a6a9c;
    --orange: #f26322;
    --white: #ffffff;
    --muted: #a9b9c6;
    --rule: #7fa6bd;
    --stage: #2b2b2c;
  }
  * { box-sizing: border-box; margin: 0; padding: 0; }
  html, body {
    width: 1200px; height: 1108px; overflow: hidden;
    background: var(--stage);
  }
  .stage {
    width: 1200px; height: 1108px;
    display: flex; align-items: center; justify-content: center; gap: 70px;
  }
  .card {
    width: 400px; height: 660px;
    border-radius: 22px;
    background: var(--navy);
    position: relative;
    overflow: hidden;
    color: var(--white);
    font-family: "Arimo", Arial, sans-serif;
  }
  .card-front {
    display: flex; flex-direction: column; align-items: center;
    padding: 126px 24px 0;
    text-align: center;
  }
  .brand-name {
    font-family: "Montserrat", Arial, sans-serif;
    font-weight: 900;
    font-size: 50px;
    letter-spacing: 1px;
    color: var(--white);
    line-height: 1;
  }
  .brand-tagline {
    margin-top: 16px;
    font-family: "Montserrat", Arial, sans-serif;
    font-weight: 800;
    font-size: 13px;
    letter-spacing: 1.5px;
    color: var(--muted);
    text-transform: uppercase;
  }
  .person-name {
    margin-top: 118px;
    font-family: "Montserrat", Arial, sans-serif;
    font-weight: 900;
    font-size: 25px;
    color: var(--orange);
    text-transform: uppercase;
    letter-spacing: 0.5px;
  }
  .person-title {
    margin-top: 4px;
    font-size: 16px;
    text-transform: uppercase;
    letter-spacing: 0.5px;
  }
  .contact-divider {
    margin-top: 18px;
    display: flex; align-items: center; gap: 8px;
  }
  .contact-divider .rule {
    width: 62px; height: 1px; background: var(--rule);
  }
  .contact-icon {
    width: 30px; height: 30px;
    background: var(--orange);
    border-radius: 5px;
    display: flex; align-items: center; justify-content: center;
  }
  .contact-list {
    margin-top: 14px;
    list-style: none;
    font-size: 18px;
    line-height: 1.45;
  }
  .card-back .brand-pattern {
    position: absolute; inset: 0;
    background: linear-gradient(160deg, var(--navy-light) 0%, var(--navy) 45%, var(--navy-deep) 100%);
  }
  .card-back .brand-mark {
    position: absolute;
    left: 0; right: 0; top: 470px;
    text-align: center;
    font-family: "Montserrat", Arial, sans-serif;
    font-weight: 900;
    font-size: 26px;
    letter-spacing: 1px;
    color: var(--white);
  }
</style>
</head>
<body>
  <main class="stage">
    <section class="card card-front" aria-label="Business card front">
      <h1 class="brand-name">QUORVANE</h1>
      <p class="brand-tagline">Quorvane Freight Company</p>

      <h2 class="person-name">Daniel Mercer</h2>
      <p class="person-title">Managing Director</p>

      <div class="contact-divider">
        <span class="rule"></span>
        <span class="contact-icon" aria-hidden="true">
          <svg width="18" height="18" viewBox="0 0 24 24"><path fill="#fff" d="M6.6 10.8a15 15 0 0 0 6.6 6.6l2.2-2.2c.3-.3.7-.4 1-.2 1.1.4 2.3.6 3.6.6.6 0 1 .4 1 1V20c0 .6-.4 1-1 1A17 17 0 0 1 3 4c0-.6.4-1 1-1h3.5c.6 0 1 .4 1 1 0 1.3.2 2.5.6 3.6.1.3 0 .7-.2 1z"/></svg>
        </span>
        <span class="contact-icon" aria-hidden="true">
          <svg width="18" height="18" viewBox="0 0 24 24"><rect x="3" y="6" width="18" height="12" rx="1" fill="#fff"/><path d="M3.5 6.5 12 13l8.5-6.5" stroke="#f26322" stroke-width="1.6" fill="none"/></svg>
        </span>
        <span class="contact-icon" aria-hidden="true">
          <svg width="18" height="18" viewBox="0 0 24 24"><circle cx="12" cy="12" r="9" fill="#fff"/><path d="M3 12h18M12 3c3 3 3 15 0 18M12 3c-3 3-3 15 0 18" stroke="#f26322" stroke-width="1.4" fill="none"/></svg>
        </span>
        <span class="rule"></span>
      </div>

      <ul class="contact-list">
        <li>055-987 654 321</li>
        <li>office@quorvanefreight.com</li>
        <li>www.quorvanefreight.com</li>
      </ul>
    </section>

    <section class="card card-back" aria-label="Business card back">
      <div class="brand-pattern" role="img" aria-label="Tonal repeating brand-name pattern across the navy background"></div>
      <p class="brand-mark">QUORVANE</p>
    </section>
  </main>
</body>
</html>
```